We are looking for a clean new looking business card.

We would like a new, clean, and modern type business card with our updated contact information. We are a small a plumbing and heating and gasfitting company who offer 24 hr emergency service as well.
We feel our logo looks best on a white background.
Our current cards are outdated, both the design and the information.

Industry/Entity Type

Plumbing and heating

Contact Information for Business Card

Logo, Name, Title, Phone#, Email, Website, "24/7 Emergency Service"

Colors
0054AA
0677BA
7BADD7
CADEEF
E8F1F8

```html
<!DOCTYPE html>
<html lang="en">
<head>
<meta charset="utf-8">
<title>Northcreek Business Card</title>
<link rel="stylesheet" href="https://fonts.googleapis.com/css2?family=Montserrat:wght@400;500;600;700;800&display=swap">
<style>
  :root {
    --navy: #0054AA;
    --blue: #0677BA;
    --sky: #7BADD7;
    --mist: #CADEEF;
    --ice: #E8F1F8;
    --bright: #27A6DC;
    --ink: #2b2b2b;
    --grey: #555b60;
    --stage: #3b3b3d;
    --white: #ffffff;
  }
  * { margin: 0; padding: 0; box-sizing: border-box; }
  html, body {
    width: 1200px; height: 1200px; overflow: hidden;
    background: var(--stage);
    font-family: "Montserrat", sans-serif;
  }
  .card {
    position: absolute;
    left: 150px;
    width: 900px; height: 514px;
    border-radius: 34px;
    overflow: hidden;
  }
  .card--front { top: 56px; background: var(--white); }
  .card--back  { top: 630px; background: var(--blue); }

  /* front: brand */
  .brand { position: absolute; right: 60px; top: 56px; text-align: center; }
  .brand__line { display: flex; align-items: center; justify-content: center; gap: 14px; }
  .brand__dot { width: 42px; height: 42px; border-radius: 50%; background: var(--bright); flex: none; }
  .brand__name {
    font-size: 52px; font-weight: 800; color: var(--blue);
    letter-spacing: 1px; line-height: 1;
  }
  .brand__tagline {
    margin-top: 12px; font-size: 12px; font-weight: 600;
    letter-spacing: 3px; color: var(--ink);
  }

  /* front: identity */
  .identity {
    position: absolute; left: 70px; top: 172px;
    padding-left: 20px;
    border-left: 6px solid var(--bright);
  }
  .identity__name {
    font-size: 44px; font-weight: 600; color: var(--bright);
    letter-spacing: 1px; line-height: 1;
  }
  .identity__title {
    font-size: 20px; font-weight: 500; color: var(--grey);
    letter-spacing: 1px; margin-top: 6px;
  }
  .contacts { position: absolute; left: 92px; top: 282px; list-style: none; }
  .contacts__row {
    display: flex; align-items: center; gap: 16px;
    font-size: 22px; color: var(--grey); height: 44px;
  }
  .contacts__row svg { width: 26px; height: 26px; flex: none; }

  /* front: emergency */
  .emergency {
    position: absolute; right: 50px; bottom: 76px;
    display: flex; align-items: center; gap: 12px;
    font-size: 28px; font-weight: 600; color: var(--blue);
    white-space: nowrap;
  }
  .emergency svg { width: 34px; height: 34px; }
  .band { position: absolute; bottom: 0; }
  .band--light { left: 0; width: 540px; height: 30px; background: var(--bright); }
  .band--dark  { right: 0; width: 352px; height: 62px; background: var(--navy); }

  /* back */
  .back-brand {
    position: absolute; inset: 0;
    display: flex; flex-direction: column; align-items: center; justify-content: center;
  }
  .back-brand__line { display: flex; align-items: center; gap: 24px; }
  .back-brand__dot { width: 80px; height: 80px; border-radius: 50%; background: var(--white); }
  .back-brand__name {
    font-size: 96px; font-weight: 800; color: var(--white);
    letter-spacing: 3px; line-height: 1;
  }
  .back-brand__tagline {
    margin-top: 20px; font-size: 22px; font-weight: 600;
    letter-spacing: 6px; color: var(--white);
  }
</style>
</head>
<body>

<section class="card card--front">
  <div class="brand">
    <div class="brand__line">
      <span class="brand__dot"></span>
      <span class="brand__name">northcreek</span>
    </div>
    <p class="brand__tagline">PLUMBING · HEATING · GASFITTING</p>
  </div>

  <div class="identity">
    <p class="identity__name">ALEX MARSH</p>
    <p class="identity__title">CEO | FOUNDER</p>
  </div>

  <ul class="contacts">
    <li class="contacts__row">
      <svg viewBox="0 0 24 24"><path fill="#27A6DC" d="M6.6 10.8a15 15 0 0 0 6.6 6.6l2.2-2.2a1 1 0 0 1 1-.25 11.4 11.4 0 0 0 3.6.57 1 1 0 0 1 1 1V20a1 1 0 0 1-1 1A17 17 0 0 1 3 4a1 1 0 0 1 1-1h3.5a1 1 0 0 1 1 1c0 1.25.2 2.45.57 3.570a1 1 0 0 1-.25 1z"/></svg>
      (555) 214-0386
    </li>
    <li class="contacts__row">
      <svg viewBox="0 0 24 24"><rect x="2" y="5" width="20" height="14" fill="#27A6DC"/><path d="M2 5l10 8 10-8M2 19l7-7M22 19l-7-7" fill="none" stroke="#fff" stroke-width="1.6"/></svg>
      info@northcreekpro.com
    </li>
    <li class="contacts__row">
      <svg viewBox="0 0 24 24" fill="none" stroke="#27A6DC" stroke-width="1.6"><circle cx="12" cy="12" r="10"/><ellipse cx="12" cy="12" rx="4.5" ry="10"/><path d="M2 12h20M4 7h16M4 17h16"/></svg>
      www.northcreekpro.com
    </li>
  </ul>

  <div class="emergency">
    <svg viewBox="0 0 24 24" fill="none" stroke="#27A6DC" stroke-width="2"><circle cx="12" cy="12" r="10"/><path d="M12 6v6l4 3"/></svg>
    24/7 Emergency Service
  </div>

  <div class="band band--light"></div>
  <div class="band band--dark"></div>
</section>

<section class="card card--back">
  <div class="back-brand">
    <div class="back-brand__line">
      <span class="back-brand__dot"></span>
      <span class="back-brand__name">northcreek</span>
    </div>
    <p class="back-brand__tagline">PLUMBING · HEATING · GASFITTING</p>
  </div>
</section>

</body>
</html>
```